Design Business Card CORAL TIDE MOWING

We have attached a copy of our Logo, we like a business card designed with logo and mobile phone number on one side that stands out maybe gloss and on the other side it can have the services we do small picture of our logo name number, I have attached an idea to this that I have seen online, this is a business owned by a woman so we like pinks black and navy
Our logo is attached in pdf
Target Market(s)
Home owners that need lawns mowed
Industry/Entity Type
Lawns and gardens
Contact Information for Business Card
Logo business Owner name Dorinda Pask mobile number 0417296054
Font styles to use
Look and feel
Each slider illustrates characteristics of the customer's brand and the style your logo design should communicate.

```html
<!DOCTYPE html>
<html lang="en">
<head>
<meta charset="UTF-8">
<title>Coral Tide Mowing – Business Card</title>
<link href="https://fonts.googleapis.com/css2?family=Open+Sans:wght@400;600;700;800&display=swap" rel="stylesheet">
<style>
  :root{
    --stage:#232323;
    --card-dark:#222226;
    --band-mid:#1c1c20;
    --band-deep:#17171a;
    --pink:#e8198c;
    --green:#3ab54a;
    --green-light:#a6c24a;
    --white:#ffffff;
    --ink:#0b0b0d;
  }
  *{box-sizing:border-box;margin:0;padding:0}
  html,body{width:1200px;height:780px;overflow:hidden;background:var(--stage)}
  body{font-family:"Open Sans",Arial,sans-serif;position:relative}
  .card{
    position:absolute;top:90px;width:343px;height:600px;border-radius:22px;overflow:hidden;
    box-shadow:0 18px 40px rgba(0,0,0,.55);
  }
  .card--front{left:215px;background:linear-gradient(225deg,var(--green-light) 0%,#6cbd4b 45%,var(--green) 100%)}
  .card--back{left:642px;background:var(--card-dark);color:var(--white)}

  .brand{position:absolute;display:flex;align-items:center;gap:10px;font-weight:800;color:var(--pink);line-height:1.05;text-transform:uppercase}
  .brand__dot{flex:none;border-radius:50%;background:var(--ink)}
  .card--front .brand{left:0;right:0;top:250px;justify-content:center;font-size:28px}
  .card--front .brand__dot{width:34px;height:34px}
  .card--back .brand{left:0;right:0;top:70px;justify-content:center;font-size:19px}
  .card--back .brand__dot{width:22px;height:22px}

  .bands{position:absolute;left:0;top:0;width:343px;height:600px}

  .owner{position:absolute;left:0;right:0;top:215px;text-align:center}
  .owner__name{font-size:30px;font-weight:700;letter-spacing:.3px}
  .owner__first{color:var(--pink)}
  .owner__last{color:var(--green)}
  .owner__role{font-size:14px;font-weight:600;margin-top:2px}

  .contact-icons{position:absolute;left:0;right:0;top:290px;display:flex;justify-content:center;gap:8px}
  .contact-icons__item{width:24px;height:24px;border-radius:50%;background:var(--pink);display:flex;align-items:center;justify-content:center}
  .contact-icons__item svg{width:14px;height:14px}

  .contact-lines{position:absolute;left:0;right:0;top:325px;text-align:center;list-style:none;font-size:14px;line-height:20px}

  .services{position:absolute;left:22px;right:22px;top:470px;text-align:center}
  .services__title{color:var(--pink);font-size:19px;font-weight:700;letter-spacing:.5px}
  .services__list{list-style:none;display:flex;flex-wrap:wrap;justify-content:center;gap:2px 10px;font-size:12.5px;margin-top:6px}
  .services__list li::before{content:"";display:inline-block;width:7px;height:7px;border-radius:50%;background:var(--pink);margin-right:5px;vertical-align:1px}
</style>
</head>
<body>

<section class="card card--front" aria-label="Business card front">
  <div class="brand"><span class="brand__dot"></span><span>Coral Tide<br>Mowing</span></div>
</section>

<section class="card card--back" aria-label="Business card back">
  <svg class="bands" viewBox="0 0 343 600" aria-hidden="true">
    <path d="M0 400 C120 440 270 420 343 300 L343 600 L0 600 Z" fill="var(--band-mid)"/>
    <path d="M0 470 C130 470 280 450 343 380 L343 600 L0 600 Z" fill="var(--band-deep)"/>
  </svg>

  <div class="brand"><span class="brand__dot"></span><span>Coral Tide Mowing</span></div>

  <div class="owner">
    <p class="owner__name"><span class="owner__first">Dorinda</span> <span class="owner__last">Pask</span></p>
    <p class="owner__role">Owner</p>
  </div>

  <div class="contact-icons">
    <span class="contact-icons__item" aria-label="Phone">
      <svg viewBox="0 0 24 24"><path fill="#fff" d="M6.6 10.8a15 15 0 0 0 6.6 6.6l2.2-2.2a1 1 0 0 1 1-.25 11.4 11.4 0 0 0 3.6.57 1 1 0 0 1 1 1V20a1 1 0 0 1-1 1A17 17 0 0 1 3 4a1 1 0 0 1 1-1h3.5a1 1 0 0 1 1 1c0 1.25.2 2.45.57 3.57a1 1 0 0 1-.25 1z"/></svg>
    </span>
    <span class="contact-icons__item" aria-label="Email">
      <svg viewBox="0 0 24 24"><rect x="3" y="6" width="18" height="12" rx="1.5" fill="#fff"/><path d="M3.5 7l8.5 6 8.5-6" stroke="var(--pink)" stroke-width="1.8" fill="none"/></svg>
    </span>
    <span class="contact-icons__item" aria-label="Website">
      <svg viewBox="0 0 24 24" fill="none" stroke="#fff" stroke-width="1.8"><circle cx="12" cy="12" r="8.5"/><ellipse cx="12" cy="12" rx="3.8" ry="8.5"/><path d="M3.5 12h17"/></svg>
    </span>
  </div>

  <ul class="contact-lines">
    <li>041 729 6054</li>
    <li>hello@coraltidemowing.com</li>
    <li>www.coraltidemowing.com</li>
  </ul>

  <div class="services">
    <h2 class="services__title">SERVICES</h2>
    <ul class="services__list">
      <li>Garden maintenance</li>
      <li>Rubbish removal</li>
      <li>Trimming</li>
      <li>Weeding</li>
      <li>Lawn care</li>
    </ul>
  </div>
</section>

</body>
</html>
```